Cutting Edge Ultra High End Investment Company & Business Card

We are an Ultra High End PRIVATE Investment Group that is known for being ULTRA EXCLUSIVE and High NET WORTH. We are kind of the Meridian Vault Onyx for the private investment space in Orange County California, we only invite new investors by referral only.
We are looking for a information only web site that has a big impact once we invite new investors to our site. It needs to be Ultra Modern, Sophisticated, and make an impact. The only contact information that will be listed on the web site is a place where if invite a new investor they can enter a code to unlock access to our members contacts (future page)
We are like the look of a full size web lay out where it has a very large full screen image background.
We are open to any fonts any colors and any designs.
Target Market(s)
Private investors for information only
Industry/Entity Type
Business
Contact Information for Business Card
Please see attached jpeg. this is a very GENERIC
Number of Pages Required
1 page
Requirements
Must have
- Modern, Cutting Edge, Big Impact
Nice to have
- All the info that currently on VR Business Card Attached
Should not have
- Boxing gloves

```html
<!DOCTYPE html>
<html lang="en">
<head>
<meta charset="utf-8">
<title>VR Investment Group</title>
<link href="https://fonts.googleapis.com/css2?family=Open+Sans:wght@300;400;600;700;800&display=swap" rel="stylesheet">
<style>
:root{
  --ink:#1c1c1c;
  --black:#0b0b0b;
  --white:#ffffff;
  --text:#6b6b6b;
  --card-dark:#2a2a2a;
  --line:#d9d9d9;
  --muted:#a8a8a8;
  --gold:#c8a45a;
}
*{margin:0;padding:0;box-sizing:border-box}
html,body{width:1200px;height:2224px;overflow:hidden}
body{font-family:"Open Sans",Arial,sans-serif;color:var(--ink);background:var(--white);position:relative}

/* hero */
.hero{position:absolute;left:0;top:0;width:1200px;height:688px;overflow:hidden}
.hero-photo{position:absolute;inset:0;background:linear-gradient(120deg,#4e555d 0%,#8d959d 30%,#bfc5cb 50%,#5f6c7b 75%,#22344d 100%)}
.topbar{position:absolute;left:0;top:0;width:1200px;height:48px;display:flex;justify-content:space-between;align-items:center;padding:0 110px 0 100px}
.social{display:flex;gap:10px}
.social span{width:28px;height:28px;border:2px solid var(--white);border-radius:50%}
.access{display:flex;align-items:center;gap:10px;font-size:12px;color:var(--white);letter-spacing:1px;text-transform:uppercase}
.access svg{flex:none}
.access input{width:150px;height:28px;border:1px solid rgba(255,255,255,.7);background:rgba(0,0,0,.25);color:var(--white);font:12px "Open Sans",Arial,sans-serif;padding:0 10px;letter-spacing:2px}
.access input::placeholder{color:#d6d6d6}
.access button{height:28px;padding:0 14px;border:0;background:var(--black);color:var(--white);font:700 11px "Open Sans",Arial,sans-serif;letter-spacing:1.5px;text-transform:uppercase}
.brand-panel{position:absolute;left:340px;top:160px;width:520px;height:380px;background:rgba(255,255,255,.42);display:flex;align-items:center;justify-content:center}
.brand-name{font-size:170px;font-weight:800;color:var(--black);letter-spacing:6px;line-height:1}

/* nav */
.mainnav{position:absolute;left:0;top:688px;width:1200px;height:84px;background:var(--black);display:flex;padding-left:160px;align-items:stretch}
.mainnav a{color:var(--white);text-decoration:none;font-size:18px;display:flex;align-items:center;justify-content:center;width:176px;text-transform:uppercase}
.mainnav a.active{background:var(--white);color:var(--black);margin-top:14px}

/* intro */
.intro{position:absolute;left:0;top:800px;width:1200px;text-align:center}
.intro-title{display:flex;justify-content:center;align-items:center;gap:24px;font-size:46px;font-weight:400;color:var(--ink)}
.intro-title .mark{width:84px;height:84px;border-radius:50%;background:radial-gradient(circle,#f3c64a,#6cb7d9 60%,#ffffff 72%)}
.intro p{width:940px;margin:24px auto 0;font-size:13px;line-height:25px;color:var(--text)}

/* services */
.services{position:absolute;left:120px;top:1140px;width:960px;display:flex;justify-content:space-between}
.card{width:280px;height:440px;border:1px solid var(--line);position:relative;background:var(--white)}
.card h3{height:104px;padding-top:14px;text-align:center;font-size:22px;font-weight:400;line-height:27px;text-transform:uppercase}
.card-body{position:absolute;left:0;bottom:0;width:100%;height:300px;background:var(--card-dark);color:var(--white);text-align:center;padding:112px 22px 0}
.card-photo{position:absolute;left:75px;top:100px;width:130px;height:130px;border-radius:50%;border:4px solid var(--white);z-index:2}
.card-body p{font-size:13px;line-height:19px;color:#e4e4e4}
.more{position:absolute;right:26px;bottom:20px;font-size:11px;font-weight:700;letter-spacing:.5px;color:var(--white)}
.p1{background:linear-gradient(180deg,#dfe3e6,#8d939a)}
.p2{background:linear-gradient(135deg,#b8d8a6,#e7c88a,#7fa1c5)}
.p3{background:linear-gradient(135deg,#e0e6ee,#9fb7cf,#5e7da0)}

/* news & testimonials */
.lower{position:absolute;left:0;top:1660px;width:1200px;height:500px;overflow:hidden}
.lower-bg{position:absolute;inset:0;background:linear-gradient(100deg,#1d2227 0%,#2f363d 40%,#3b3630 70%,#1c1f22 100%)}
.lower h2{position:absolute;top:30px;font-size:34px;font-weight:400;color:var(--white);text-transform:uppercase}
.news-rule{position:absolute;left:120px;top:84px;width:590px;height:1px;background:rgba(255,255,255,.35)}
.news-item{position:absolute;top:108px;width:270px;color:var(--white)}
.news-img{width:270px;height:130px;position:relative}
.news-img .date{position:absolute;left:0;bottom:0;background:var(--black);font-size:10px;padding:4px 10px}
.n1{background:linear-gradient(135deg,#3b6fb3,#d9a441,#6fa6d6)}
.n2{background:linear-gradient(135deg,#d7dde2,#e9b35a,#8cb4cf)}
.news-item h4{font-size:12px;font-weight:600;margin-top:12px;text-transform:uppercase}
.meta{font-size:10px;color:var(--muted);margin-top:8px;display:flex;gap:26px}
.news-item p{font-size:11px;line-height:17px;color:#d0d0d0;margin-top:10px}
.btn{display:inline-block;margin-top:26px;background:var(--black);color:var(--white);font-size:10px;font-weight:700;padding:8px 14px;text-transform:uppercase}
.testimonial{position:absolute;left:820px;top:96px;width:270px;color:var(--white)}
.avatar{width:94px;height:94px;border-radius:50%;margin:0 auto;background:linear-gradient(160deg,#7a4a36,#c79a7c)}
.t-name{text-align:center;font-size:12px;margin-top:10px;color:#dcdcdc}
.quote{display:flex;gap:12px;margin-top:38px}
.quote b{font-size:44px;line-height:36px;font-family:Georgia,serif}
.quote p{font-size:12px;line-height:19px;color:#e0e0e0}
.arrows{position:absolute;right:110px;bottom:26px;display:flex;gap:14px}

/* footer */
.footer{position:absolute;left:0;top:2160px;width:1200px;height:64px;background:var(--black);color:var(--white);display:flex;align-items:center;justify-content:space-between;padding:0 110px 0 40px;font-size:12px}
.footer nav{display:flex;gap:58px}
</style>
</head>
<body>

<header class="hero">
  <div class="hero-photo" role="img" aria-label="Close-up photo of a padlock resting on a bank card"></div>
  <div class="topbar">
    <div class="social"><span></span><span></span><span></span></div>
    <form class="access" action="#">
      <svg width="12" height="14" viewBox="0 0 12 14"><rect x="1" y="6" width="10" height="7.5" fill="#fff"/><path d="M3 6V4a3 3 0 0 1 6 0v2" fill="none" stroke="#fff" stroke-width="1.6"/></svg>
      <label for="invite">Members</label>
      <input id="invite" type="text" placeholder="Invite code">
      <button type="submit">Unlock</button>
    </form>
  </div>
  <div class="brand-panel"><span class="brand-name">VR</span></div>
</header>

<nav class="mainnav">
  <a class="active" href="#">Home</a>
  <a href="#">About us</a>
  <a href="#">Services</a>
  <a href="#">News</a>
  <a href="#">Contact us</a>
</nav>

<section class="intro">
  <h1 class="intro-title"><span class="mark"></span>VR Investment Group</h1>
  <p>Sed ut perspiciatis unde omnis iste natus error sit voluptatem accusantium doloremque laudantium, totam rem aperiam, eaque ipsa quae ab illo inventore veritatis et quasi architecto beatae vitae dicta sunt explicabo. Nemo enim ipsam voluptatem quia voluptas sit aspernatur aut odit aut fugit, sed quia consequuntur magni dolores eos qui ratione voluptatem sequi nesciunt. Neque porro quisquam est, qui dolorem ipsum quia dolor sit amet, consectetur, adipisci velit, sed quia non numquam eius modi tempora incidunt ut labore et dolore magnam aliquam quaerat voluptatem. Ut enim ad minima veniam, quis nostrum exercitationem ullam corporis suscipit laboriosam, nisi ut aliquid ex ea commodi consequatur. Quis autem vel eum iure reprehenderit qui in ea voluptate velit esse quam nihil molestiae consequatur, vel illum qui dolorem eum fugiat quo voluptas nulla pariatur.</p>
</section>

<section class="services">
  <article class="card">
    <h3>Broker<br>Comparison</h3>
    <div class="card-photo p1" role="img" aria-label="Portrait photo of a businessman"></div>
    <div class="card-body">
      <p>Lorem ipsum dolor sit amet, consectetur adipisic elit. Proin ultricies vestibulum velit sed dum et condimentum nonummy lorem ipsum. Vivamus sed dolore ipsum consectetur.</p>
      <span class="more">READ MORE &gt;</span>
    </div>
  </article>
  <article class="card">
    <h3>Investment<br>Consulting</h3>
    <div class="card-photo p2" role="img" aria-label="Photo of financial charts and coins"></div>
    <div class="card-body">
      <p>Lorem ipsum dolor sit amet, consectetur adipisic elit. Proin ultricies vestibulum velit sed dum et condimentum nonummy lorem ipsum. Vivamus sed dolore ipsum consectetur.</p>
      <span class="more">READ MORE &gt;</span>
    </div>
  </article>
  <article class="card">
    <h3>Investment<br>Solutions</h3>
    <div class="card-photo p3" role="img" aria-label="Photo of a business chart on a desk"></div>
    <div class="card-body">
      <p>Lorem ipsum dolor sit amet, consectetur adipisic elit. Proin ultricies vestibulum velit sed dum et condimentum nonummy lorem ipsum. Vivamus sed dolore ipsum consectetur.</p>
      <span class="more">READ MORE &gt;</span>
    </div>
  </article>
</section>

<section class="lower">
  <div class="lower-bg" role="img" aria-label="Dark background photo of a desk with financial papers"></div>
  <h2 style="left:120px">Latest News</h2>
  <div class="news-rule"></div>
  <article class="news-item" style="left:120px">
    <div class="news-img n1" role="img" aria-label="Photo of financial graphs on a screen"><span class="date">18 AUG 2015</span></div>
    <h4>Neque porro quisquam est qui</h4>
    <div class="meta"><span>By admin</span><span>Comments 0</span></div>
    <p>Lorem ipsum dolor sit amet, consectetur adipiscing elit. Nam ut tortor tincidunt, aliquam nisi eget, pulvinar lorem. Sed vitae ante ut tellus.</p>
    <span class="btn">Read more</span>
  </article>
  <article class="news-item" style="left:420px">
    <div class="news-img n2" role="img" aria-label="Photo of documents, pen and calculator"><span class="date">18 AUG 2015</span></div>
    <h4>Neque porro quisquam est qui</h4>
    <div class="meta"><span>By admin</span><span>Comments 0</span></div>
    <p>Lorem ipsum dolor sit amet, consectetur adipiscing elit. Nam ut tortor tincidunt, aliquam nisi eget, pulvinar lorem. Sed vitae ante ut tellus.</p>
    <span class="btn">Read more</span>
  </article>
  <h2 style="left:832px">Testimonials</h2>
  <div class="testimonial">
    <div class="avatar" role="img" aria-label="Portrait photo of a client"></div>
    <div class="t-name">Sarah Whitmore</div>
    <div class="quote"><b>&ldquo;</b><p>Lorem Ipsum is simply dummy text of the printing and typesetting industry. Lorem Ipsum has been the industry's standard dummy text ever since.</p></div>
  </div>
  <div class="arrows">
    <svg width="14" height="20" viewBox="0 0 14 20"><path d="M11 2L3 10l8 8" fill="none" stroke="#fff" stroke-width="2.5"/></svg>
    <svg width="14" height="20" viewBox="0 0 14 20"><path d="M3 2l8 8-8 8" fill="none" stroke="#fff" stroke-width="2.5"/></svg>
  </div>
</section>

<footer class="footer">
  <span>&copy; ALL RIGHTS RESERVED, VR INVESTMENT, 2015</span>
  <nav><span>Home</span><span>About Us</span><span>News</span><span>Services</span><span>Contact Us</span></nav>
</footer>

</body>
</html>
```